business card design for luxurious real estate brand

using the attached logo, i am looking for a 2-sided business card design. the back should be the gold logo on black background. the front needs to include: gold logo, name, phone, email, and website

Industry/Entity Type

real estate

Contact Information for Business Card

logo, name, email, phone, website

Font styles to use
Sans Serif

```html
<!DOCTYPE html>
<html lang="en">
<head>
<meta charset="utf-8">
<title>Casa Verano — Business Card</title>
<link href="https://fonts.googleapis.com/css2?family=Poppins:wght@400;500&display=swap" rel="stylesheet">
<style>
  :root {
    --stage: #2b2e34;
    --card: #121519;
    --band: #1f2630;
    --band-light: #2c3542;
    --gold: #d9b86a;
    --gold-soft: #b8944e;
  }
  * { margin: 0; padding: 0; box-sizing: border-box; }
  html, body { width: 1200px; height: 780px; overflow: hidden; }
  body {
    background: var(--stage);
    font-family: "Poppins", sans-serif;
    position: relative;
  }
  .card {
    position: absolute;
    top: 240px;
    width: 520px;
    height: 300px;
    border-radius: 22px;
    background: var(--card);
    overflow: hidden;
    box-shadow: 0 18px 40px rgba(0,0,0,0.45);
  }
  .card--front { left: 50px; }
  .card--back { left: 630px; }
  .card__bands { position: absolute; inset: 0; width: 100%; height: 100%; }
  .brand {
    position: absolute;
    display: flex;
    align-items: center;
    gap: 14px;
    color: var(--gold);
    font-weight: 500;
    font-size: 24px;
    letter-spacing: 0.28em;
    text-transform: uppercase;
  }
  .brand__mark {
    width: 22px; height: 22px;
    background: var(--gold);
    flex: none;
  }
  .card--front .brand { left: 50%; top: 50%; transform: translate(-50%, -50%); }
  .card--back .brand { right: 34px; top: 128px; font-size: 19px; gap: 11px; }
  .card--back .brand__mark { width: 17px; height: 17px; }
  .contact {
    position: absolute;
    left: 34px;
    top: 100px;
    list-style: none;
    display: flex;
    flex-direction: column;
    gap: 12px;
  }
  .contact__item {
    display: flex;
    align-items: center;
    gap: 12px;
    color: #e8dcc0;
    font-size: 14px;
    font-weight: 400;
  }
  .contact__icon { width: 22px; height: 22px; flex: none; }
</style>
</head>
<body>

<section class="card card--front" aria-label="Card front">
  <svg class="card__bands" viewBox="0 0 520 300" aria-hidden="true">
    <defs>
      <linearGradient id="bandShade" x1="0" y1="0" x2="1" y2="1">
        <stop offset="0" stop-color="var(--band)"/>
        <stop offset="0.6" stop-color="var(--band-light)"/>
        <stop offset="1" stop-color="var(--band)"/>
      </linearGradient>
    </defs>
    <polygon points="0,0 280,0 0,62" fill="url(#bandShade)"/>
    <line x1="0" y1="58" x2="270" y2="0" stroke="var(--gold)" stroke-width="1"/>
    <line x1="0" y1="66" x2="300" y2="0" stroke="var(--gold-soft)" stroke-width="0.8"/>
    <polygon points="520,300 240,300 520,238" fill="url(#bandShade)"/>
    <line x1="520" y1="242" x2="250" y2="300" stroke="var(--gold)" stroke-width="1"/>
    <line x1="520" y1="234" x2="220" y2="300" stroke="var(--gold-soft)" stroke-width="0.8"/>
  </svg>
  <div class="brand"><span class="brand__mark"></span><span class="brand__name">Casa Verano</span></div>
</section>

<section class="card card--back" aria-label="Card back">
  <svg class="card__bands" viewBox="0 0 520 300" aria-hidden="true">
    <polygon points="0,0 280,0 0,62" fill="url(#bandShade)"/>
    <line x1="0" y1="58" x2="270" y2="0" stroke="var(--gold)" stroke-width="1"/>
    <line x1="0" y1="66" x2="300" y2="0" stroke="var(--gold-soft)" stroke-width="0.8"/>
    <polygon points="520,300 240,300 520,238" fill="url(#bandShade)"/>
    <line x1="520" y1="242" x2="250" y2="300" stroke="var(--gold)" stroke-width="1"/>
    <line x1="520" y1="234" x2="220" y2="300" stroke="var(--gold-soft)" stroke-width="0.8"/>
  </svg>

  <ul class="contact">
    <li class="contact__item">
      <svg class="contact__icon" viewBox="0 0 22 22" aria-hidden="true">
        <polygon points="11,1 20,6 20,16 11,21 2,16 2,6" fill="var(--gold)"/>
        <path d="M8 6.5l2 2.2-1.2 1.4c.7 1.4 1.7 2.4 3.1 3.1l1.4-1.2 2.2 2-1.2 1.6c-3.6-.4-6.9-3.7-7.3-7.3z" fill="var(--card)"/>
      </svg>
      <span>+100 555 0199</span>
    </li>
    <li class="contact__item">
      <svg class="contact__icon" viewBox="0 0 22 22" aria-hidden="true">
        <polygon points="11,1 20,6 20,16 11,21 2,16 2,6" fill="var(--gold)"/>
        <circle cx="11" cy="11" r="5" fill="none" stroke="var(--card)" stroke-width="1.2"/>
        <path d="M6 11h10M11 6c-2.2 2.8-2.2 7.2 0 10M11 6c2.2 2.8 2.2 7.2 0 10" fill="none" stroke="var(--card)" stroke-width="1"/>
      </svg>
      <span>www.casaverano.com</span>
    </li>
    <li class="contact__item">
      <svg class="contact__icon" viewBox="0 0 22 22" aria-hidden="true">
        <polygon points="11,1 20,6 20,16 11,21 2,16 2,6" fill="var(--gold)"/>
        <path d="M6 11l10-4-3 9-2-3.5z" fill="var(--card)"/>
      </svg>
      <span>@casaverano.com</span>
    </li>
  </ul>

  <div class="brand"><span class="brand__mark"></span><span class="brand__name">Casa Verano</span></div>
</section>

</body>
</html>
```